TALMERA Stationary and Biz Card design
TALMERA Economic Development Company
TALMERA Stationary and Biz Card design - Financial Services
Creative Brief
Professional
Dennis P Wexford
CEO
PO BOX 782 FAIRHOLT, MAINE 04987
dennis@talmeraco.example
talmeraco.example
Looking for designs that encompass the strength and integrity of the logo.

```html
<!DOCTYPE html>
<html lang="en">
<head>
<meta charset="utf-8">
<title>TALMERA Business Card</title>
<link rel="stylesheet" href="https://fonts.googleapis.com/css2?family=Open+Sans:wght@400;600;700&display=swap">
<style>
  :root {
    --page-bg: #eceae6;
    --card-bg: #ffffff;
    --navy: #1f3a64;
    --text-grey: #555a61;
    --decor-light: #e9ebee;
    --decor-mid: #d9dde3;
    --card-shadow: rgba(0, 0, 0, 0.18);
  }
  * { box-sizing: border-box; margin: 0; padding: 0; }
  html, body {
    width: 1200px;
    height: 535px;
    overflow: hidden;
    background: var(--page-bg);
    font-family: "Open Sans", Arial, sans-serif;
  }
  .canvas {
    position: relative;
    width: 1200px;
    height: 535px;
  }
  .card {
    position: absolute;
    top: 136px;
    width: 564px;
    height: 333px;
    background: var(--card-bg);
    box-shadow: 0 3px 10px var(--card-shadow);
    overflow: hidden;
  }
  .card--front { left: 24px; }
  .card--back { left: 619px; }

  .card__decor {
    position: absolute;
    left: 0;
    top: 0;
    width: 250px;
    height: 333px;
    background: linear-gradient(100deg, var(--decor-mid) 0%, var(--decor-light) 55%, var(--card-bg) 100%);
  }

  .wordmark {
    position: absolute;
    font-weight: 600;
    color: var(--navy);
    letter-spacing: 0.28em;
    white-space: nowrap;
  }
  .card--front .wordmark {
    left: 276px;
    top: 108px;
    font-size: 30px;
  }
  .card--back .wordmark {
    left: 0;
    width: 564px;
    text-align: center;
    top: 142px;
    font-size: 34px;
    padding-left: 0.28em;
  }

  .holder {
    position: absolute;
    left: 29px;
    top: 234px;
  }
  .holder__name {
    font-size: 15px;
    font-weight: 700;
    color: var(--navy);
  }
  .holder__title {
    font-size: 12px;
    color: var(--text-grey);
    margin-top: 2px;
  }

  .contact {
    position: absolute;
    left: 283px;
    top: 180px;
    list-style: none;
    font-size: 11.5px;
    color: var(--text-grey);
  }
  .contact__item {
    display: flex;
    align-items: center;
    height: 23px;
  }
  .contact__icon {
    width: 12px;
    height: 12px;
    margin-right: 10px;
    fill: var(--text-grey);
  }
  .address {
    position: absolute;
    left: 283px;
    top: 298px;
    font-size: 11.5px;
    color: var(--text-grey);
  }

  .website {
    position: absolute;
    left: 0;
    width: 564px;
    top: 208px;
    text-align: center;
    font-size: 13px;
    color: var(--text-grey);
  }
  .website strong { color: var(--navy); font-weight: 700; }
</style>
</head>
<body>
<main class="canvas">

  <section class="card card--front" aria-label="Business card front">
    <div class="card__decor" role="img" aria-label="Faint decorative backdrop panel"></div>

    <div class="wordmark">TALMERA</div>

    <div class="holder">
      <p class="holder__name">Dennis P Wexford</p>
      <p class="holder__title">CEO</p>
    </div>

    <ul class="contact">
      <li class="contact__item">
        <svg class="contact__icon" viewBox="0 0 12 12" aria-hidden="true"><rect x="3" y="0.5" width="6" height="11" rx="1.2"/><rect x="4" y="2" width="4" height="6" fill="#fff"/></svg>
        310 555 0148
      </li>
      <li class="contact__item">
        <svg class="contact__icon" viewBox="0 0 12 12" aria-hidden="true"><rect x="3" y="0.5" width="6" height="3.5"/><rect x="0.5" y="4" width="11" height="5" rx="1"/><rect x="3" y="7.5" width="6" height="4" fill="#fff" stroke="#555a61" stroke-width="1"/></svg>
        207 555 0173
      </li>
      <li class="contact__item">
        <svg class="contact__icon" viewBox="0 0 12 12" aria-hidden="true"><rect x="0.5" y="2" width="11" height="8" rx="1"/><path d="M1 2.6 6 6.6 11 2.6" fill="none" stroke="#fff" stroke-width="1.1"/></svg>
        dennis@talmeraco.example
      </li>
      <li class="contact__item">
        <svg class="contact__icon" viewBox="0 0 12 12" aria-hidden="true"><circle cx="6" cy="6" r="5.5"/><path d="M0.8 6h10.4M6 0.6c-2.4 2.8-2.4 8 0 10.8M6 0.6c2.4 2.8 2.4 8 0 10.8" fill="none" stroke="#fff" stroke-width="0.9"/></svg>
        www.talmeraco.example
      </li>
    </ul>

    <p class="address">PO Box 782 Fairholt, Maine 04987</p>
  </section>

  <section class="card card--back" aria-label="Business card back">
    <div class="card__decor" role="img" aria-label="Faint decorative backdrop panel"></div>

    <div class="wordmark">TALMERA</div>

    <p class="website">www.<strong>talmeraco</strong>.example</p>
  </section>

</main>
</body>
</html>
```